Gombrevo business card

Based on company logo and website given , to design a business card temple. Slogan "Your furry friends deserves the best"
Color style please refer to our website

```html
<!DOCTYPE html>
<html lang="en">
<head>
<meta charset="utf-8">
<title>Gombrevo Business Card</title>
<link rel="stylesheet" href="https://fonts.googleapis.com/css2?family=Oswald:wght@300;400;500;600;700&display=swap">
<style>
  :root {
    --page-bg: #ffffff;
    --card-bg: #0b2c2b;
    --gold: #bdae2b;
    --white: #ffffff;
    --card-shadow: 0 2px 6px rgba(0, 0, 0, 0.28);
  }
  * { margin: 0; padding: 0; box-sizing: border-box; }
  html, body {
    width: 1200px;
    height: 1200px;
    overflow: hidden;
    background: var(--page-bg);
  }
  .canvas {
    position: relative;
    width: 1200px;
    height: 1200px;
    font-family: "Oswald", sans-serif;
  }
  .card {
    position: absolute;
    left: 248px;
    width: 711px;
    height: 427px;
    background: var(--card-bg);
    box-shadow: var(--card-shadow);
  }
  .card--front { top: 158px; }
  .card--back { top: 622px; }

  .brand-name {
    color: var(--gold);
    font-family: "Oswald", sans-serif;
    font-weight: 500;
    line-height: 1;
    white-space: nowrap;
  }
  .card--front .brand-name {
    position: absolute;
    left: 108px;
    top: 112px;
    font-size: 46px;
    letter-spacing: 0.5px;
  }

  .identity {
    position: absolute;
    left: 108px;
    top: 224px;
  }
  .identity__name {
    color: var(--white);
    font-weight: 700;
    font-size: 28px;
    line-height: 1.15;
    letter-spacing: 0.4px;
  }
  .identity__role {
    color: var(--gold);
    font-weight: 400;
    font-size: 19px;
    line-height: 1.3;
    letter-spacing: 0.3px;
  }

  .contact {
    position: absolute;
    left: 357px;
    top: 226px;
  }
  .contact__rule {
    width: 42px;
    height: 1.5px;
    background: var(--gold);
    margin-bottom: 5px;
  }
  .contact__line {
    color: var(--white);
    font-weight: 500;
    font-size: 19px;
    line-height: 25px;
    letter-spacing: 0.2px;
  }

  .tagline {
    position: absolute;
    left: 0;
    right: 0;
    top: 342px;
    text-align: center;
    color: var(--gold);
    font-weight: 400;
    font-size: 18px;
    letter-spacing: 0.2px;
  }

  .card--back {
    display: flex;
    align-items: center;
    justify-content: center;
  }
  .card--back .brand-name {
    font-size: 100px;
    letter-spacing: 1px;
  }
</style>
</head>
<body>
  <main class="canvas">
    <section class="card card--front">
      <div class="brand-name">Gombrevo</div>

      <div class="identity">
        <div class="identity__name">GOMBREVO</div>
        <div class="identity__role">FOUNDER</div>
      </div>

      <div class="contact">
        <div class="contact__rule"></div>
        <div class="contact__line">+61 03 90418266</div>
        <div class="contact__line">info@gombrevo.com.au</div>
      </div>

      <p class="tagline">"Your Furry Friends Deserves The Best"</p>
    </section>

    <section class="card card--back">
      <div class="brand-name">Gombrevo</div>
    </section>
  </main>
</body>
</html>
```